Commercial printing and sign company printed advertisement.

We're wanting a new look for our printed advertisements. We've been in business for 40 years and have been pushing hard the last couple of years to grow our business. Our target market is changing and our client base is changing. I am looking for advertisement that appeals to larger companies. However, we are not stuffy people so I would like the ads to convey our professionalism but also stand out with color and have a fun side. I'm currently needing advertisements for a printed magazine, printed newspaper, web ads and a table top at a local restaurant. We have our traditional four color logo (swoosh) as well as a simpler single color option. I am attaching various ads we have done previously so you can see what we have. It is important for these ads to convey the different things we do - as we do alot!

```html
<!DOCTYPE html>
<html lang="en">
<head>
<meta charset="utf-8">
<title>Halden Press – 40 Years Advertisement</title>
<link rel="stylesheet" href="https://fonts.googleapis.com/css2?family=Archivo+Black&family=Jost:wght@400;500&display=swap">
<style>
  :root {
    --stage: #3b79bf;
    --paper-top: #ffffff;
    --paper-bottom: #ececec;
    --brand-red: #cc1029;
    --ink: #1c1a1a;
    --muted: #6b6b6b;
    --rb-red: #d0122c;
    --rb-orange: #f47b20;
    --rb-yellow: #f7cf1d;
    --rb-green: #1f8a4c;
    --rb-blue: #1b5fb0;
    --rb-purple: #8a2a9c;
    --wash-yellow: #f6e08a;
    --wash-peach: #f2b98f;
    --wash-blue: #bcd3ea;
  }
  html, body {
    margin: 0;
    width: 1200px;
    height: 1063px;
    overflow: hidden;
    background: var(--stage);
  }
  .poster {
    position: absolute;
    left: 240px;
    top: 25px;
    width: 720px;
    height: 1012px;
    display: block;
  }
  .brand-name { font-family: "Archivo Black", sans-serif; fill: var(--brand-red); }
  .kicker { font-family: "Jost", sans-serif; font-weight: 400; fill: var(--ink); letter-spacing: 14px; }
  .headline { font-family: "Archivo Black", sans-serif; fill: var(--brand-red); }
  .tagline { font-family: "Jost", sans-serif; font-weight: 500; fill: var(--ink); letter-spacing: 3px; }
  .web-address { font-family: "Jost", sans-serif; font-weight: 400; fill: var(--muted); letter-spacing: 8px; }
  .numeral { font-family: "Archivo Black", sans-serif; }
</style>
</head>
<body>
<svg class="poster" viewBox="0 0 875 1230" xmlns="http://www.w3.org/2000/svg">
  <defs>
    <linearGradient id="paper" x1="0" y1="0" x2="0" y2="1">
      <stop offset="0" stop-color="var(--paper-top)"/>
      <stop offset="1" stop-color="var(--paper-bottom)"/>
    </linearGradient>
    <linearGradient id="rainbow" x1="0" y1="0" x2="1" y2="1">
      <stop offset="0" stop-color="var(--rb-red)"/>
      <stop offset="0.35" stop-color="var(--rb-orange)"/>
      <stop offset="0.5" stop-color="var(--rb-yellow)"/>
      <stop offset="0.65" stop-color="var(--rb-green)"/>
      <stop offset="0.82" stop-color="var(--rb-blue)"/>
      <stop offset="1" stop-color="var(--rb-purple)"/>
    </linearGradient>
    <linearGradient id="rainbow-stroke" x1="1" y1="0" x2="0" y2="1">
      <stop offset="0" stop-color="var(--rb-red)"/>
      <stop offset="0.35" stop-color="var(--rb-yellow)"/>
      <stop offset="0.65" stop-color="var(--rb-green)"/>
      <stop offset="1" stop-color="var(--rb-purple)"/>
    </linearGradient>
    <radialGradient id="wash" cx="0.5" cy="0.5" r="0.5">
      <stop offset="0" stop-color="var(--wash-yellow)" stop-opacity="0.8"/>
      <stop offset="0.6" stop-color="var(--wash-peach)" stop-opacity="0.45"/>
      <stop offset="1" stop-color="var(--wash-blue)" stop-opacity="0"/>
    </radialGradient>
    <linearGradient id="collage" x1="0" y1="0" x2="1" y2="1">
      <stop offset="0" stop-color="#e9c08a"/>
      <stop offset="0.4" stop-color="#d28c5c"/>
      <stop offset="0.7" stop-color="#c8c35a"/>
      <stop offset="1" stop-color="#8aa6b8"/>
    </linearGradient>
  </defs>

  <rect class="paper" width="875" height="1230" fill="url(#paper)"/>

  <!-- frame -->
  <g class="frame" fill="none" stroke="url(#rainbow)">
    <path stroke-width="4" d="M856 229 V23 H18 V1213 H856 V858 M856 733 V360"/>
    <path stroke-width="1.5" d="M845 229 V35 H29 V1202 H845 V858 M845 733 V360"/>
  </g>

  <!-- watercolour wash -->
  <ellipse role="img" aria-label="Soft watercolour wash in yellow, peach and pale blue" cx="470" cy="620" rx="330" ry="330" fill="url(#wash)"/>

  <!-- numeral filled with print-shop imagery -->
  <text class="numeral" role="img" aria-label="Large numeral 40 filled with a collage of printing press and print-shop photos" x="80" y="852" font-size="560" letter-spacing="-40" fill="url(#collage)">40</text>

  <!-- brand name -->
  <text class="brand-name" x="160" y="355" font-size="84">Halden Press</text>

  <!-- diagonal accents -->
  <line x1="838" y1="327" x2="678" y2="536" stroke="url(#rainbow-stroke)" stroke-width="5"/>
  <line x1="773" y1="391" x2="321" y2="979" stroke="var(--ink)" stroke-width="1.5"/>
  <line x1="443" y1="861" x2="281" y2="1069" stroke="var(--ink)" stroke-width="12"/>

  <!-- headline block -->
  <text class="kicker" x="516" y="726" font-size="27">BUILT ON</text>
  <text class="headline" x="500" y="794" font-size="62">40 YEARS</text>
  <text class="headline" x="504" y="832" font-size="31">of Getting It Done</text>

  <!-- footer -->
  <text class="tagline" x="463" y="1101" font-size="23" text-anchor="middle">PROVIDING PRINTING FOR</text>
  <text class="tagline" x="468" y="1131" font-size="23" text-anchor="middle">BUSINESSES THAT EXPECT RELIABILITY AND RESULTS</text>
  <text class="web-address" x="437" y="1164" font-size="17" text-anchor="middle">WWW.HALDENPRESS.COM</text>
</svg>
</body>
</html>
```